Brindle Gardenworks Business Card

An eye catching, yet simple business card that includes;

1. our logo
2. office phone - 5127730194
3. email - brindlegardenworks@mailnest.example
4. website - www.brindlegardenworks.example
5. instagram - @brindlegardenworksrvt

```html
<!DOCTYPE html>
<html lang="en">
<head>
<meta charset="utf-8">
<title>Brindle Gardenworks Business Card</title>
<link href="https://fonts.googleapis.com/css2?family=Roboto:wght@400;700&display=swap" rel="stylesheet">
<style>
  :root {
    --backdrop: #3a3a3c;
    --card-dark: #231d1a;
    --card-light: #ffffff;
    --accent: #b5661f;
    --ink: #2e2e2e;
    --ink-soft: #555555;
    --rule: #9a9a9a;
    --sweep-fill: #f1f1f1;
  }
  * { box-sizing: border-box; margin: 0; padding: 0; }
  html, body {
    width: 1200px; height: 900px; overflow: hidden;
    background: var(--backdrop);
    font-family: "Roboto", Arial, sans-serif;
  }
  .sheet {
    width: 1200px; height: 900px;
    display: flex; align-items: center; justify-content: center; gap: 40px;
  }
  .card {
    position: relative;
    width: 540px; height: 309px;
    border-radius: 18px;
    overflow: hidden;
    box-shadow: 0 10px 30px rgba(0,0,0,0.35);
  }
  /* Back side */
  .card-back {
    background: var(--card-dark);
    display: flex; align-items: center; justify-content: center; gap: 14px;
  }
  .brand-dot {
    width: 26px; height: 26px; border-radius: 50%;
    background: var(--accent);
  }
  .brand-name {
    color: #ffffff;
    font-weight: 700;
    font-size: 36px;
    letter-spacing: 1px;
    text-transform: uppercase;
  }
  /* Front side */
  .card-front { background: var(--card-light); }
  .sweep { position: absolute; inset: 0; }
  .front-brand {
    position: absolute; left: 28px; top: 86px; width: 190px;
    display: flex; align-items: center; gap: 8px;
  }
  .front-brand .brand-dot { width: 16px; height: 16px; flex: none; }
  .front-brand .brand-name {
    color: var(--accent); font-size: 19px; line-height: 1.15; letter-spacing: 0.5px;
  }
  .divider {
    position: absolute; left: 236px; top: 62px;
    width: 1px; height: 132px; background: var(--rule);
  }
  .details { position: absolute; left: 256px; top: 66px; }
  .person-name {
    color: var(--accent); font-weight: 700; font-size: 17px;
    text-transform: uppercase; letter-spacing: 0.3px;
  }
  .person-role { color: var(--ink); font-size: 13px; margin-top: 2px; }
  .contact-list { list-style: none; margin-top: 14px; }
  .contact-list li {
    display: flex; align-items: center; gap: 8px;
    color: var(--ink-soft); font-size: 12.5px; line-height: 21px;
  }
  .contact-icon {
    width: 13px; height: 13px; flex: none;
    background: var(--accent); border-radius: 3px;
    display: flex; align-items: center; justify-content: center;
  }
  .contact-icon svg { width: 9px; height: 9px; }
</style>
</head>
<body>
<main class="sheet">
  <section class="card card-back" aria-label="Card back">
    <span class="brand-dot"></span>
    <span class="brand-name">Brindle Gardenworks</span>
  </section>

  <section class="card card-front" aria-label="Card front">
    <svg class="sweep" viewBox="0 0 540 309" preserveAspectRatio="none" aria-hidden="true">
      <path d="M0 190 C 120 230, 300 250, 540 309 L 0 309 Z" fill="var(--sweep-fill)"/>
      <path d="M0 190 C 120 230, 300 250, 540 309" fill="none" stroke="var(--accent)" stroke-width="3"/>
    </svg>

    <div class="front-brand">
      <span class="brand-dot"></span>
      <span class="brand-name">Brindle Gardenworks</span>
    </div>

    <div class="divider"></div>

    <div class="details">
      <p class="person-name">Tobias R. Lindqvist</p>
      <p class="person-role">Founder &amp; CEO</p>
      <ul class="contact-list">
        <li>
          <span class="contact-icon"><svg viewBox="0 0 10 10"><path d="M2 1 L4 1 L4.6 3 L3.5 3.8 C4 5 5 6 6.2 6.5 L7 5.4 L9 6 L9 8 C5 8.5 1.5 5 2 1 Z" fill="#fff"/></svg></span>
          5127730194
        </li>
        <li>
          <span class="contact-icon"><svg viewBox="0 0 10 10"><rect x="1" y="2.5" width="8" height="5" fill="none" stroke="#fff" stroke-width="1"/><path d="M1 2.5 L5 5.5 L9 2.5" fill="none" stroke="#fff" stroke-width="1"/></svg></span>
          brindlegardenworks@mailnest.example
        </li>
        <li>
          <span class="contact-icon"><svg viewBox="0 0 10 10"><circle cx="5" cy="5" r="3.6" fill="none" stroke="#fff" stroke-width="1"/><path d="M1.4 5 H8.6 M5 1.4 C3.5 3.5 3.5 6.5 5 8.6 M5 1.4 C6.5 3.5 6.5 6.5 5 8.6" fill="none" stroke="#fff" stroke-width="0.8"/></svg></span>
          www.brindlegardenworks.example
        </li>
        <li>
          <span class="contact-icon"></span>
          @brindlegardenworksrvt
        </li>
      </ul>
    </div>
  </section>
</main>
</body>
</html>
```